Brexmoor Solutions
Not Necessary
Simple
Marlon Teague
N/A
marlon@brexmoorsolutions.example
http://www.brexmoorsolutions.example
Brexmoor Solutions is a custom development/software development firm. Specialize on web and mobile development.
I'd be interested in what a double sided business card looks like but may settle on a one-sided card.
Your discretion on whether to use logo's font or another - whatever looks best.
Logo and fonts

```html
<!DOCTYPE html>
<html lang="en">
<head>
<meta charset="utf-8">
<title>Brexmoor Solutions — Business Card</title>
<link rel="stylesheet" href="https://fonts.googleapis.com/css2?family=Open+Sans:wght@400;600;700&display=swap">
<style>
  :root {
    --bg: #2b2b2d;
    --card-white: #ffffff;
    --card-shade: #e9ecef;
    --brand-blue: #1f5f95;
    --brand-blue-dark: #0f3d66;
    --brand-blue-light: #3f86c0;
    --text-grey: #6b6f74;
    --text-dark: #3a3d41;
  }
  * { box-sizing: border-box; margin: 0; padding: 0; }
  html, body { width: 1200px; height: 901px; overflow: hidden; }
  body {
    background: var(--bg);
    font-family: "Open Sans", Arial, sans-serif;
    display: flex;
    align-items: center;
    justify-content: center;
    gap: 40px;
  }
  .card {
    position: relative;
    width: 520px;
    height: 300px;
    border-radius: 22px;
    overflow: hidden;
  }
  .card--front {
    background: linear-gradient(160deg, var(--card-white) 55%, var(--card-shade));
  }
  .edge-tab {
    position: absolute;
    width: 9px;
    height: 64px;
    background: var(--brand-blue);
  }
  .edge-tab--left { left: 0; bottom: 34px; border-radius: 0 5px 5px 0; }
  .edge-tab--right { right: 0; top: 38px; border-radius: 5px 0 0 5px; }
  .brand-name {
    position: absolute;
    left: 36px;
    top: 34px;
    font-weight: 600;
    font-size: 34px;
    letter-spacing: 0.5px;
    color: var(--brand-blue);
    line-height: 1;
  }
  .person-name {
    position: absolute;
    left: 36px;
    top: 104px;
    font-weight: 700;
    font-size: 18px;
    color: var(--brand-blue);
  }
  .person-title {
    position: absolute;
    left: 36px;
    top: 168px;
    font-size: 13px;
    color: var(--text-grey);
  }
  .contact-list {
    position: absolute;
    left: 36px;
    top: 200px;
    list-style: none;
  }
  .contact-item {
    display: flex;
    align-items: center;
    gap: 9px;
    font-size: 13px;
    color: var(--text-dark);
    height: 21px;
  }
  .contact-icon { width: 13px; height: 13px; flex: none; }
  .card--back {
    background: radial-gradient(ellipse at 50% 45%, var(--brand-blue-light), var(--brand-blue) 55%, var(--brand-blue-dark));
    display: flex;
    flex-direction: column;
    align-items: center;
    justify-content: center;
    gap: 14px;
  }
  .back-brand {
    font-weight: 600;
    font-size: 40px;
    color: var(--card-white);
    letter-spacing: 0.5px;
  }
  .back-web {
    font-size: 13px;
    color: var(--card-white);
    opacity: 0.85;
    letter-spacing: 1px;
  }
</style>
</head>
<body>
  <section class="card card--front" aria-label="Business card front">
    <span class="edge-tab edge-tab--left"></span>
    <span class="edge-tab edge-tab--right"></span>
    <div class="brand-name">Brexmoor Solutions</div>
    <div class="person-name">Marlon Teague</div>
    <div class="person-title">N/A</div>
    <ul class="contact-list">
      <li class="contact-item">
        <svg class="contact-icon" viewBox="0 0 13 13" aria-hidden="true"><rect x="3" y="0.5" width="7" height="12" rx="1.5" fill="var(--text-grey)"/><rect x="4.3" y="2" width="4.4" height="7" fill="#fff"/></svg>
        555-014-7362
      </li>
      <li class="contact-item">
        <svg class="contact-icon" viewBox="0 0 13 13" aria-hidden="true"><rect x="0.5" y="2.5" width="12" height="8" rx="1" fill="var(--text-grey)"/><path d="M1 3l5.5 4.5L12 3" stroke="#fff" stroke-width="1.1" fill="none"/></svg>
        marlon@brexmoorsolutions.example
      </li>
      <li class="contact-item">
        <svg class="contact-icon" viewBox="0 0 13 13" aria-hidden="true"><circle cx="6.5" cy="6.5" r="6" fill="var(--text-grey)"/><ellipse cx="6.5" cy="6.5" rx="2.6" ry="6" stroke="#fff" stroke-width="0.9" fill="none"/><path d="M0.8 6.5h11.4" stroke="#fff" stroke-width="0.9"/></svg>
        www.brexmoorsolutions.example
      </li>
    </ul>
  </section>

  <section class="card card--back" aria-label="Business card back">
    <div class="back-brand">Brexmoor Solutions</div>
    <div class="back-web">www.brexmoorsolutions.example</div>
  </section>
</body>
</html>
```